Business Card for Managing Partner Investment Fund

To create a business card template for an investment fund manager. Business card should be more professional in nature, not too colorful, more upscale, and created using the attached logos and fund name files. I would prefer a black or gray color scheme, but am open to the use of color as well. I would prefer a double sided business card, but open to single sided business card designs as well. The business card should include: name, title, and contact information, as well as logo and company name. I would prefer a more stream-lined, simple business card design.
Updates
Address: 4190 NE 38th Ter. Ocala, FL 34470
Email: talvin47@quorimail.net
Phone: 561-347-9162
Title: managing partner
Name: Dorian Velsky
Fund Name: Ambergate Capital
Logos can be found in files attached to the brief
Target Market(s)
potential investors, other fund managers
Industry/Entity Type
Finance
Contact Information for Business Card
Name on card: Dorian Velsky
Title: Managing Partner
Colors
Designer to choose colors to be used in the design.
Requirements
Must have
- Phone number
- email address
- physical address
- title
- name
- logo
- Fund name
Nice to have
- simple layout
Should not have
- too many colors, busy fonts,

```html
<!DOCTYPE html>
<html lang="en">
<head>
<meta charset="utf-8">
<title>Ambergate Capital — Business Card</title>
<link rel="stylesheet" href="https://fonts.googleapis.com/css2?family=Montserrat:wght@600&family=Arimo:wght@400&display=swap">
<style>
  :root {
    --backdrop: #a19e9b;
    --card-dark: #57524e;
    --card-mid: #8c8078;
    --card-light: #cdbbb0;
    --ink-light: #ecdad0;
    --ink-dark: #55504c;
  }
  * { margin: 0; padding: 0; box-sizing: border-box; }
  html, body {
    width: 1200px;
    height: 1200px;
    overflow: hidden;
    background: var(--backdrop);
  }
  .canvas {
    position: relative;
    width: 1200px;
    height: 1200px;
  }
  .card {
    position: absolute;
    left: 214px;
    width: 770px;
    height: 427px;
  }
  .card--front {
    top: 106px;
    background: linear-gradient(160deg, var(--card-dark) 0%, var(--card-mid) 55%, var(--card-light) 100%);
  }
  .card--back {
    top: 654px;
    background: linear-gradient(160deg, var(--card-light) 0%, var(--card-mid) 50%, var(--card-dark) 100%);
  }
  .holder-name {
    position: absolute;
    left: 50px;
    top: 60px;
    font-family: "Montserrat", sans-serif;
    font-weight: 600;
    font-size: 29px;
    letter-spacing: 0.5px;
    text-transform: uppercase;
    color: var(--ink-light);
  }
  .holder-title {
    position: absolute;
    left: 50px;
    top: 100px;
    font-family: "Arimo", sans-serif;
    font-size: 22px;
    color: var(--ink-light);
  }
  .contact {
    position: absolute;
    left: 54px;
    top: 283px;
    list-style: none;
    font-family: "Arimo", sans-serif;
    font-size: 20px;
    line-height: 34px;
    color: var(--ink-light);
  }
  .brand-mark {
    position: absolute;
    font-family: "Montserrat", sans-serif;
    font-weight: 600;
    text-transform: uppercase;
    text-align: center;
  }
  .brand-mark--small {
    right: 48px;
    top: 316px;
    font-size: 17px;
    line-height: 24px;
    letter-spacing: 2px;
    color: var(--ink-dark);
  }
  .brand-mark--large {
    left: 0;
    right: 0;
    top: 180px;
    font-size: 44px;
    line-height: 58px;
    letter-spacing: 4px;
    color: var(--ink-light);
  }
</style>
</head>
<body>
<div class="canvas">
  <section class="card card--front">
    <h1 class="holder-name">Dorian Velsky</h1>
    <p class="holder-title">Managing Partner</p>
    <ul class="contact">
      <li>561-347-9162</li>
      <li>4190 NE 38th Ter. Ocala, FL 34470</li>
      <li>talvin47@quorimail.net</li>
    </ul>
    <p class="brand-mark brand-mark--small">Ambergate<br>Capital</p>
  </section>

  <section class="card card--back">
    <p class="brand-mark brand-mark--large">Ambergate<br>Capital</p>
  </section>
</div>
</body>
</html>
```